Business Card Design

We sell fish products to corporate food companies who then turn these products into final food products for consumers

Industry/Entity Type

Business

Contact Information for Business Card

I need a corporate business card template for a fish products business. We would like it be professional for use in dealing with multi national companies. This company business card template will be used by multiple employees so the following fields must be open to edit (Name, Phone Number and Email address)

```html
<!DOCTYPE html>
<html lang="en">
<head>
<meta charset="utf-8">
<title>Harbor Crest Seafoods – Business Card</title>
<link rel="stylesheet" href="https://fonts.googleapis.com/css2?family=Marcellus&family=Michroma&display=swap">
<style>
  :root {
    --paper: #ffffff;
    --brand-blue: #0a5aa9;
    --brand-green: #6bc28d;
    --bubble-tint: #c9d9ea;
    --bubble-fade: rgba(201, 217, 234, 0);
    --band-text: #ffffff;
  }
  * { margin: 0; padding: 0; box-sizing: border-box; }
  html, body {
    width: 1200px;
    height: 702px;
    overflow: hidden;
    background: var(--paper);
  }
  .business-card {
    position: relative;
    width: 1200px;
    height: 702px;
    background: var(--paper);
    overflow: hidden;
  }
  .bubble-field {
    position: absolute;
    left: 94px;
    top: 55px;
    width: 625px;
    height: 277px;
    background: radial-gradient(ellipse at 40% 50%, var(--bubble-tint) 0%, var(--bubble-fade) 70%);
    opacity: 0.7;
  }
  .brand-mark {
    position: absolute;
    left: 540px;
    top: 150px;
    width: 124px;
    height: 124px;
    border-radius: 50%;
    background: var(--brand-blue);
  }
  .brand-name {
    position: absolute;
    left: 0;
    top: 362px;
    width: 100%;
    text-align: center;
    font-family: "Marcellus", serif;
    font-weight: 400;
    color: var(--brand-blue);
  }
  .brand-name__main {
    display: block;
    font-size: 100px;
    line-height: 1;
    letter-spacing: 1px;
  }
  .brand-name__sub {
    display: block;
    margin-top: 18px;
    font-size: 50px;
    line-height: 1;
    letter-spacing: 16px;
    padding-left: 16px;
  }
  .contact-band {
    position: absolute;
    left: 0;
    top: 583px;
    width: 1200px;
    height: 119px;
  }
  .contact-band svg { display: block; }
  .field {
    position: absolute;
    top: 598px;
    font-family: "Michroma", sans-serif;
    font-size: 22px;
    line-height: 1;
    color: var(--band-text);
  }
  .field--name { left: 202px; }
  .field--contact { left: 751px; }
</style>
</head>
<body>
  <main class="business-card">
    <div class="bubble-field" role="img" aria-label="Soft drifting water bubbles decoration"></div>

    <div class="brand-mark" aria-hidden="true"></div>

    <h1 class="brand-name">
      <span class="brand-name__main">HARBOR CREST</span>
      <span class="brand-name__sub">SEAFOODS</span>
    </h1>

    <div class="contact-band" aria-hidden="true">
      <svg width="1200" height="119" viewBox="0 0 1200 119">
        <rect x="0" y="0" width="1200" height="119" fill="var(--brand-green)"/>
        <path d="M 640 0 L 1200 0 L 1200 119 L 553 119 C 575 70 603 25 640 0 Z" fill="var(--brand-blue)"/>
      </svg>
    </div>

    <p class="field field--name">name</p>
    <p class="field field--contact">phone|e-mail</p>
  </main>
</body>
</html>
```